Online-Marketing Material für Nachhilfeschule
Quintessa hat superschnell gearbeitet, vorher selbst recherchiert, um sofort das zu meiner Webseite passende Produkt zu erstellen. Da es eine Kooperation in diesem Fall gab, hat er beide Webseiten für seine Produktvorschläge als Wunschvorstellung ausgesucht und angewendet. Perfekt! That's quintessa! Thank you!
Zielgruppe
Ich habe am 1.7. eine Nachhilfeschule gegründet. Nun möchte ich ein Pilotprojekt starten, um Schülern in der Abiturklasse - Gymnasium oder Berufsschule - , die exzellente Zensuren wollen, zu herausragenden Noten zu verhelfen.
Dieser Banner wird durch den Lehrer den Schülern per Email oder WhatsApp überreicht.
Ich stelle mir ein junges und dynamisches Design vor. Das schwarz/grüne Logo der Fahrschule gefällt mir besser (wenn das andere Eurer Meinung nach besser passt, geht auch das). Das Schwarz-weiß-Logo vom Wissensnest muss aber dominanter sein!
Mein Kooperationspartner, eine Fahrschule, stellt ihre Räume zur Verfügung. Meine Gegenleistung: Nennung in der Werbung.
Aufgabenstellung
Zielgruppe: Abiturienten,
- die Gas geben wollen, damit sie bessere Chancen am Arbeitsmarkt haben.
- die bereit sind, 4 Samstage herzugeben, um noch mehr zu lernen ...
- die selbst, oder deren Eltern, bereit sind, für diese Chancen Geld auszugeben
- die bei der Anmeldung aufgezeigt bekommen, dass das Bonbon eine Vermittlung zu ihrem Wunschunternehmen und ihrer Wunschposition ist.
Das Bonbon bitte Fahrschul-Logo-grün machen, vielleicht auch mit Punkten - vom Wissensnest-Logo ...
Die Texte sind in der Word-Datei. Wichtig: Sie müssen bearbeitet werden können, da sich die Daten wie z.B. Datum, Preis, Fächer, etc. ändern können. Wenn die Kurse angenommen werden, wird der Gewinner zukünftig meine gesamte Werbung gestalten -> CI

```html
<!DOCTYPE html>
<html lang="de">
<head>
<meta charset="utf-8">
<title>Wissensnest – Ich geb Gas fürs Abi!</title>
<link rel="stylesheet" href="https://fonts.googleapis.com/css2?family=Poppins:ital,wght@0,400;0,500;0,600;0,700;0,800;1,500;1,900&family=Raleway:wght@500;600;700;800&display=swap">
<style>
  :root {
    --green: #58f01a;
    --green-soft: #d6f7c4;
    --ink: #231f20;
    --paper: #ffffff;
    --cream: #f6f2ef;
    --white: #ffffff;
  }
  * { margin: 0; padding: 0; box-sizing: border-box; }
  html, body { width: 848px; height: 1200px; overflow: hidden; background: var(--paper); }
  .flyer {
    position: relative; width: 848px; height: 1200px; overflow: hidden;
    background: var(--paper); color: var(--ink);
    font-family: "Poppins", sans-serif;
  }
  .brand {
    position: absolute; top: 78px; left: 0; width: 848px;
    display: flex; justify-content: center; align-items: center; gap: 18px;
  }
  .brand-dot { width: 62px; height: 62px; border-radius: 50%; background: var(--ink); }
  .brand-name { font-family: "Raleway", sans-serif; font-weight: 500; font-size: 64px; letter-spacing: 1px; color: var(--ink); }
  .headline {
    position: absolute; top: 216px; left: 0; width: 848px; text-align: center;
    font-family: "Poppins", sans-serif; font-weight: 900; font-style: italic;
    font-size: 58px; letter-spacing: -0.5px; line-height: 1; white-space: nowrap;
  }
  .headline .accent { color: var(--green); }
  .intro-green {
    position: absolute; top: 302px; left: 78px; width: 692px; height: 54px;
    background: var(--green); color: var(--white);
    font-family: "Raleway", sans-serif; font-weight: 700; font-size: 31px;
    padding-left: 15px; line-height: 54px; z-index: 2; white-space: nowrap;
    box-shadow: 0 4px 8px rgba(0,0,0,0.25);
  }
  .intro-dark {
    position: absolute; top: 346px; left: 34px; width: 780px; height: 63px;
    background: var(--ink); color: var(--white);
    font-family: "Raleway", sans-serif; font-weight: 800; font-size: 31.5px;
    text-align: center; line-height: 66px; white-space: nowrap;
  }
  .pole {
    position: absolute; top: 428px; left: 0; width: 848px; text-align: center;
    font-family: "Raleway", sans-serif; font-weight: 800; font-size: 26.5px; white-space: nowrap;
  }
  .bonus-title {
    position: absolute; top: 480px; left: 234px;
    font-family: "Raleway", sans-serif; font-weight: 700; font-size: 31px; color: var(--green);
  }
  .bonus-left, .bonus-right {
    position: absolute; font-family: "Raleway", sans-serif; font-weight: 500; font-size: 23px; white-space: nowrap;
  }
  .bonus-left { top: 524px; left: 182px; }
  .bonus-right { top: 526px; left: 475px; }
  .bonus-visual {
    position: absolute; top: 490px; left: 376px; width: 90px; height: 90px;
    background: var(--green-soft); border-radius: 6px;
  }
  .info-area { position: absolute; top: 930px; left: 0; width: 848px; height: 215px; background: var(--cream); }
  .wave { position: absolute; top: 0; left: 0; width: 848px; height: 1200px; }
  .fact-tag {
    position: absolute; background: var(--green); color: var(--white);
    font-family: "Poppins", sans-serif; font-weight: 600; font-size: 25px;
    height: 44px; line-height: 46px; padding: 0 15px; transform: rotate(-2deg); white-space: nowrap;
  }
  .fact-value {
    position: absolute; color: var(--white);
    font-family: "Poppins", sans-serif; font-weight: 700; font-size: 19px; line-height: 24px; white-space: nowrap;
  }
  .signup-label { position: absolute; top: 1020px; left: 67px; font-family: "Raleway", sans-serif; font-weight: 600; font-size: 21px; white-space: nowrap; }
  .signup-phone { position: absolute; top: 1045px; left: 66px; font-family: "Poppins", sans-serif; font-weight: 700; font-size: 32px; color: var(--green); white-space: nowrap; }
  .partner-label { position: absolute; top: 998px; left: 668px; font-family: "Poppins", sans-serif; font-style: italic; font-weight: 500; font-size: 19px; white-space: nowrap; }
  .partner-brand { position: absolute; top: 1044px; left: 540px; display: flex; align-items: center; gap: 10px; white-space: nowrap; }
  .partner-square { width: 22px; height: 22px; background: var(--green); flex: none; }
  .partner-name { font-family: "Poppins", sans-serif; font-weight: 700; font-size: 20px; color: var(--ink); }
  .footer { position: absolute; top: 1143px; left: 0; width: 848px; height: 57px; background: var(--ink); color: var(--white);
    text-align: center; line-height: 57px; font-family: "Poppins", sans-serif; font-weight: 700; font-size: 19px; }
</style>
</head>
<body>
<main class="flyer">
  <header class="brand">
    <span class="brand-dot"></span>
    <span class="brand-name">Wissensnest</span>
  </header>

  <h1 class="headline">„ICH GEB <span class="accent">GAS FÜRS</span> ABI!“</h1>

  <p class="intro-green">Du stehst kurz vorm Abi und hast in dir das</p>
  <p class="intro-dark">ICH WILL BERUFLICH ERFOLGREICH SEIN-GEN?</p>

  <p class="pole">Dann gib Gas und du bist in der Pole-Position!</p>

  <p class="bonus-title">Zugabe:</p>
  <p class="bonus-left">Unbezahlbares</p>
  <div class="bonus-visual" role="img" aria-label="Platz für die Illustration eines grünen Bonbons"></div>
  <p class="bonus-right">für Durchstarter!</p>

  <div class="info-area"></div>

  <svg class="wave" viewBox="0 0 848 1200" aria-hidden="true">
    <path fill="var(--ink)" d="M0,622 C80,612 150,604 205,601 C215,604 190,622 200,627 C240,634 380,604 470,605 C480,608 465,618 490,623 C560,634 700,590 848,589 L848,958 C780,950 600,955 430,962 C380,966 345,975 352,968 C385,960 380,945 330,945 C230,945 100,978 40,970 C25,966 30,958 40,952 C25,946 10,943 0,942 Z"/>
  </svg>

  <section class="facts">
    <div class="fact-tag" style="top:648px;left:64px;">wann?</div>
    <p class="fact-value" style="top:704px;left:78px;">21 Januar 2023</p>

    <div class="fact-tag" style="top:648px;left:268px;">Womit?</div>
    <p class="fact-value" style="top:704px;left:283px;">Mathe oder Englisch</p>

    <div class="fact-tag" style="top:648px;left:543px;">Wie oft?</div>
    <p class="fact-value" style="top:704px;left:560px;">An 4 Samstagen,<br>je 2 x 90 Minuten</p>

    <div class="fact-tag" style="top:790px;left:61px;">Wie viele?</div>
    <p class="fact-value" style="top:846px;left:78px;">2 bis 1 Schüler</p>

    <div class="fact-tag" style="top:790px;left:280px;">Welcher Preis?</div>
    <p class="fact-value" style="top:846px;left:294px;">290 Euro, inklusive<br>Lernmaterialien</p>

    <div class="fact-tag" style="top:788px;left:543px;">Location?</div>
    <p class="fact-value" style="top:846px;left:560px;">Kurvenwerk Fahrschule,<br>Lindenallee 7,<br>Musterstadt</p>
  </section>

  <p class="signup-label">Mehr Infos zur Anmeldung unter</p>
  <p class="signup-phone">+49 170 000 12 345</p>

  <p class="partner-label">Ihre Partner:</p>
  <div class="partner-brand">
    <span class="partner-square"></span>
    <span class="partner-name">Kurvenwerk Fahrschule</span>
  </div>

  <footer class="footer">www.wissensnest.de</footer>
</main>
</body>
</html>
```